Business card for event manager / organizer "velmora tandem"

Draft of a new valuable business card for my company.
Events, personnel service providers, festivals

```html
<!DOCTYPE html>
<html lang="de">
<head>
<meta charset="utf-8">
<title>velmora tandem – Visitenkarte</title>
<link href="https://fonts.googleapis.com/css2?family=Lato:wght@300;400;700;900&display=swap" rel="stylesheet">
<style>
  :root {
    --stage: #2b2f38;
    --paper: #ffffff;
    --ink: #1c1a1d;
    --text-grey: #4a4a4a;
    --orange: #e8731f;
    --back-card: #221e22;
    --tagline-grey: #bdbdbd;
  }
  * { margin: 0; padding: 0; box-sizing: border-box; }
  html, body {
    width: 1200px; height: 800px; overflow: hidden;
    background: var(--stage);
    font-family: "Lato", sans-serif;
  }
  .canvas { position: relative; width: 1200px; height: 800px; }

  .card {
    position: absolute; left: 390px; width: 420px; height: 240px;
    overflow: hidden;
  }
  .card--front { top: 130px; background: var(--paper); }
  .card--back { top: 430px; background: var(--back-card); }

  .event-photo {
    position: absolute; top: 0; right: 0; width: 250px; height: 240px;
    background:
      linear-gradient(to right, var(--paper) 0%, rgba(255,255,255,0) 30%),
      radial-gradient(ellipse at 60% 20%, #c9c6ef 0%, rgba(201,198,239,0) 55%),
      linear-gradient(180deg, #a9a6d8 0%, #d8cfd6 40%, #e2b68f 75%, #d98a45 100%);
  }

  .brand { position: absolute; display: flex; flex-direction: column; }
  .brand__name {
    display: flex; align-items: center; gap: 8px;
    font-weight: 900; letter-spacing: -0.3px; line-height: 1; white-space: nowrap;
  }
  .brand__mark { background: var(--orange); flex: none; }
  .brand__tagline { font-weight: 400; white-space: nowrap; }

  .card--front .brand { left: 21px; top: 22px; }
  .card--front .brand__name { font-size: 22px; color: var(--ink); }
  .card--front .brand__mark { width: 40px; height: 40px; }
  .card--front .brand__tagline {
    font-size: 7px; color: var(--ink); margin: 10px 0 0 42px;
  }

  .owner { position: absolute; left: 21px; top: 101px; }
  .owner__name {
    font-size: 16px; font-weight: 700; color: var(--orange);
    letter-spacing: 0.2px; line-height: 1.2;
  }
  .owner__role { font-size: 12px; color: var(--text-grey); line-height: 1.3; }

  .contact-list {
    position: absolute; left: 21px; top: 142px; list-style: none;
  }
  .contact-list li {
    display: flex; align-items: center; gap: 6px;
    font-size: 12px; color: var(--text-grey); height: 13.4px; white-space: nowrap;
  }
  .contact-list svg { width: 9px; height: 9px; flex: none; fill: var(--orange); }

  .card--back .brand { left: 0; right: 0; top: 82px; align-items: center; }
  .card--back .brand__name { font-size: 30px; color: #ffffff; gap: 10px; }
  .card--back .brand__mark { width: 56px; height: 56px; }
  .card--back .brand__tagline {
    font-size: 9.5px; color: var(--tagline-grey); margin-top: 6px; letter-spacing: 0.2px;
  }
</style>
</head>
<body>
<main class="canvas">

  <section class="card card--front">
    <div class="event-photo" role="img" aria-label="Foto: Brautpaar tanzt unter Konfetti und Funkenfontänen auf einer Hochzeitsfeier"></div>

    <div class="brand">
      <div class="brand__name"><span class="brand__mark"></span>velmora tandem</div>
      <div class="brand__tagline">…weil jedes Fest echte Profis braucht!</div>
    </div>

    <div class="owner">
      <div class="owner__name">JONAS BRENNER</div>
      <div class="owner__role">Inhaber</div>
    </div>

    <ul class="contact-list">
      <li>
        <svg viewBox="0 0 10 10"><path d="M2 0.5 L3.6 2.6 L2.8 3.6 C3.4 5 5 6.6 6.4 7.2 L7.4 6.4 L9.5 8 L8.4 9.5 C4.5 9.2 0.8 5.5 0.5 1.6 Z"/></svg>
        030 41 276 58 90
      </li>
      <li>
        <svg viewBox="0 0 10 10"><path d="M2.5 0 H7.5 V10 H2.5 Z M3.4 1 V8 H6.6 V1 Z M4.5 8.5 H5.5 V9.3 H4.5 Z"/></svg>
        0170 482 31 67
      </li>
      <li>
        <svg viewBox="0 0 10 10"><rect x="0.5" y="0.5" width="9" height="9" rx="1.5"/></svg>
        /velmoratandem
      </li>
      <li>
        <svg viewBox="0 0 10 10"><path d="M0.5 2 H9.5 V8 H0.5 Z M1.3 2.6 L5 5.4 L8.7 2.6 Z" fill-rule="evenodd"/></svg>
        info@velmora-tandem.de
      </li>
      <li>
        <svg viewBox="0 0 10 10"><circle cx="5" cy="5" r="4.3" fill="none" stroke="var(--orange)" stroke-width="1"/><path d="M0.7 5 H9.3 M5 0.7 V9.3" stroke="var(--orange)" stroke-width="0.8"/><ellipse cx="5" cy="5" rx="2" ry="4.3" fill="none" stroke="var(--orange)" stroke-width="0.8"/></svg>
        www.velmora-tandem.de
      </li>
      <li>
        <svg viewBox="0 0 10 10"><path d="M5 0.3 C7.2 0.3 8.6 1.9 8.6 3.8 C8.6 6.2 5 9.7 5 9.7 C5 9.7 1.4 6.2 1.4 3.8 C1.4 1.9 2.8 0.3 5 0.3 Z M5 2.3 A1.5 1.5 0 1 0 5 5.3 A1.5 1.5 0 1 0 5 2.3 Z" fill-rule="evenodd"/></svg>
        Lindenweg 12, 10115 Berlin
      </li>
    </ul>
  </section>

  <section class="card card--back">
    <div class="brand">
      <div class="brand__name"><span class="brand__mark"></span>velmora tandem</div>
      <div class="brand__tagline">…weil jedes Fest echte Profis braucht!</div>
    </div>
  </section>

</main>
</body>
</html>
```